Brightmoor - online education agent and consultancy

Online education provider for business to business market needs a dynamic, modern and mobile friendly website. We have the shell view www.kavolent.com but it is boring!
I will need to add courses to the website - Business, Health and Wellbeing, Digital, Aviation.
I am targeting mainly services based industries - so blue collar workers, living in the outer suburbs, will be studying online and most likely from home.
They need to feel safe and secure - we are reputable and importantly can support them all the way to course completion.
What makes us stand out from everyone else - we dont offer any courses - we pick and choose the best courses, with the best providers and only offer quality.
We take the time to find out what the student really wants to achieve and match them with the right education provider.

Target Market(s)

Business to Business - HR managers, People and Culture Managers, employees who are 25+ years currently working wanting to further their careers with accredited qualifications

Industry/Entity Type

Education

Number of Pages Required

5+ page

Font styles to use
Sans Serif

Colors
00a990
acd036
0792cd
a54499
f37122

Requirements
Must have
• Mobile functionality - view on zorvix/zorvixtab
• Home page
• Courses section
• Contact us
• Payment checkout to be added
Nice to have
• Fresh, inviting, images that reflect the difference we will make - supporting people through the whole journey.
• It needs to be inviting - homely but modern
Should not have
• Black, dark colours

```html
<!DOCTYPE html>
<html lang="en">
<head>
<meta charset="utf-8">
<title>Novelya – Brightmoor</title>
<link rel="stylesheet" href="https://fonts.googleapis.com/css2?family=Raleway:wght@300;400;500;600&family=Open+Sans:wght@400&display=swap">
<style>
  :root {
    --green: #acd036;
    --green-light: #c2e05a;
    --green-dark: #8cbf26;
    --green-deep: #4f9a12;
    --blue: #0792cd;
    --orange: #f7a21b;
    --ink: #2a2a2a;
    --body: #555555;
    --white: #ffffff;
  }
  * { box-sizing: border-box; margin: 0; padding: 0; }
  html, body { width: 1200px; height: 1005px; overflow: hidden; background: var(--white); }
  .page { position: relative; width: 1200px; height: 1005px; font-family: "Open Sans", sans-serif; }

  .site-header { position: absolute; left: 0; top: 0; width: 1200px; height: 127px; }
  .brand { position: absolute; left: 462px; top: 44px; display: flex; align-items: center; gap: 10px; }
  .brand-name { font-family: "Raleway", sans-serif; font-weight: 300; font-size: 50px; letter-spacing: 4px; color: var(--green-dark); line-height: 1; }
  .brand-dot { width: 18px; height: 18px; border-radius: 50%; background: var(--green-dark); }
  .phone { position: absolute; left: 910px; top: 79px; display: flex; align-items: center; gap: 6px; }
  .phone-icon { width: 30px; height: 30px; }
  .phone-number { font-size: 21px; color: #444; }

  .main-nav { position: absolute; left: 0; top: 127px; width: 1200px; height: 58px;
    background: linear-gradient(to bottom, var(--green-light), var(--green-dark)); display: flex; padding-left: 170px; }
  .nav-item { height: 58px; display: flex; align-items: center; justify-content: center;
    font-family: "Raleway", sans-serif; font-weight: 500; font-size: 17.5px; color: var(--white); }
  .nav-item + .nav-item { border-left: 1px solid rgba(255,255,255,0.35); }
  .nav-item.is-active { background: linear-gradient(to bottom, #7fbf22, var(--green-deep)); }

  .hero { position: absolute; left: 0; top: 185px; width: 1200px; height: 299px;
    background:
      radial-gradient(ellipse 260px 220px at 470px 120px, rgba(232,196,170,0.85), rgba(232,196,170,0) 70%),
      radial-gradient(ellipse 220px 200px at 1000px 200px, rgba(150,150,170,0.7), rgba(150,150,170,0) 70%),
      linear-gradient(90deg, #5e4a3c 0%, #8a6a52 14%, #c9a07c 32%, #b58a6c 52%, #8d8a96 70%, #a9a2a8 86%, #8a8690 100%);
    border-bottom: 1px solid #d0d0d0; }

  .intro { position: absolute; left: 145px; top: 549px; width: 570px; }
  .intro-title { font-family: "Raleway", sans-serif; font-weight: 400; font-size: 30px; color: var(--ink); letter-spacing: 0.5px; }
  .intro-text { position: absolute; left: 3px; width: 570px; font-size: 13px; line-height: 17.6px; color: var(--body); letter-spacing: -0.1px; }
  .intro-text.p1 { top: 55px; }
  .intro-text.p2 { top: 111px; }
  .intro-text.p3 { top: 163px; }
  .feature-image { position: absolute; left: 727px; top: 551px; width: 339px; height: 224px;
    background:
      radial-gradient(ellipse 200px 110px at 170px 120px, rgba(180,140,95,0.55), rgba(180,140,95,0) 75%),
      linear-gradient(160deg, #ecd3ad 0%, #dcb587 55%, #c9985f 100%); }

  .site-footer { position: absolute; left: 0; top: 884px; width: 1200px; height: 121px; background: var(--blue); }
  .footer-link { position: absolute; top: 34px; font-family: "Raleway", sans-serif; font-weight: 600; font-size: 14px; color: var(--white); }
  .copyright { position: absolute; left: 127px; top: 65px; font-size: 11.5px; color: var(--white); }
  .social { position: absolute; left: 926px; top: 35px; display: flex; gap: 10px; }
  .social-link { font-family: "Raleway", sans-serif; font-weight: 600; font-size: 14px; color: var(--white); }
</style>
</head>
<body>
<div class="page">
  <header class="site-header">
    <div class="brand"><span class="brand-name">NOVELYA</span><span class="brand-dot"></span></div>
    <div class="phone">
      <svg class="phone-icon" viewBox="0 0 30 30" aria-hidden="true">
        <circle cx="15" cy="15" r="15" fill="var(--orange)"/>
        <path d="M10 8.5c1-.8 2-.6 2.6.4l1.2 2c.4.8.2 1.5-.5 2l-.9.6c.7 1.6 2 3 3.6 3.7l.6-.9c.5-.7 1.2-.9 2-.5l2 1.2c1 .6 1.2 1.6.4 2.6-1.3 1.6-3.3 1.8-5.6.4-2.2-1.3-4.1-3.2-5.4-5.4-1.4-2.3-1.2-4.3.4-5.6z" fill="none" stroke="#fff" stroke-width="1.6" stroke-linejoin="round"/>
      </svg>
      <span class="phone-number">1300 48 31 62</span>
    </div>
  </header>

  <nav class="main-nav">
    <a class="nav-item" style="width:108px">HOME</a>
    <a class="nav-item is-active" style="width:199px">BRIGHTMOOR</a>
    <a class="nav-item" style="width:194px">OUR COURSES</a>
    <a class="nav-item" style="width:167px">LET'S CHAT</a>
    <a class="nav-item" style="width:197px">ABOUT NOVELYA</a>
  </nav>

  <div class="hero" role="img" aria-label="Photo of young women studying in a library"></div>

  <section class="intro">
    <h1 class="intro-title">BRIGHTMOOR</h1>
    <p class="intro-text p1">Brightmoor is NOVELYA's own unique program that has been specifically crafted to provide the best learning outcome for your employees.</p>
    <p class="intro-text p2">We commence our relationship with you and your business focussing on the most appropriate approach and courses for learning and growth.</p>
    <p class="intro-text p3">Our student support, mentor and development program provides reassurance to you and your business that employees are receiving all the support they need to grow their career and importantly take what they have learnt and apply it to the everyday.</p>
  </section>
  <div class="feature-image" role="img" aria-label="Photo of wooden letter blocks spelling LIFE on a wooden table"></div>

  <footer class="site-footer">
    <a class="footer-link" style="left:127px">HOME</a>
    <a class="footer-link" style="left:212px">BRIGHTMOOR</a>
    <a class="footer-link" style="left:363px">OUR COURSES</a>
    <a class="footer-link" style="left:509px">LET'S CHAT</a>
    <a class="footer-link" style="left:636px">ABOUT NOVELYA</a>
    <p class="copyright">© 2016 Company Name&nbsp; All right reserved&nbsp; Term of Use</p>
    <div class="social" aria-label="Social links">
      <a class="social-link">Qeto</a><a class="social-link">Vusa</a><a class="social-link">Lorn</a><a class="social-link">Gimo</a>
    </div>
  </footer>
</div>
</body>
</html>
```